IT CEO and Real Estate Investor

It should include two roles and be a two sided card (both roles can be one a single side with a creative view or on different sides).
Card must be creative and interesting, but still professional.
Phone countries(USA/Russia) might be as flags or words, whatever works better.
Boris Melnovetz
Skype: boris_m
E-mail: melnovetz@quorbamail.com
Facebook: plavbook.example/melnovetz
Linkedin: trelnet.example/in/melnovetz
Phone (US): 1(555)316-2947
Phone (RUS): 7(955)482-3170
First role:
Pex Lattor (pexlattor.example) - include logo or part of logo (the $)
E-Commerce Automation Solutions
Founder/CEO/CTO
Second role:
Real Estate Investor
Cleveland, OH
UPDATE:
Let's do one side as logo only and all information on the other side - I don't like designs with information on both sides.
I also really liked designs on black (or other dark) background

```html
<!DOCTYPE html>
<html lang="en">
<head>
<meta charset="utf-8">
<title>Pex Lattor business card</title>
<link rel="stylesheet" href="https://fonts.googleapis.com/css2?family=Source+Sans+3:wght@400;600;700&display=swap">
<style>
  :root {
    --brand-blue: #08aeec;
    --brand-blue-light: #2bb8ef;
    --paper: #ffffff;
    --backdrop-top: #c9c9c9;
    --backdrop-bottom: #ffffff;
    --divider: rgba(255,255,255,0.35);
    --text-light: #ffffff;
  }
  * { margin: 0; padding: 0; box-sizing: border-box; }
  html, body { width: 1200px; height: 900px; overflow: hidden; }
  body {
    position: relative;
    background: linear-gradient(180deg, var(--backdrop-top) 0%, #e2e2e2 55%, var(--backdrop-bottom) 100%);
    font-family: "Source Sans 3", "Myriad Pro", sans-serif;
    color: var(--text-light);
  }
  .card {
    position: absolute;
    top: 306px;
    width: 439px;
    height: 271px;
    border-radius: 12px;
    overflow: hidden;
  }
  .card--front { left: 149px; background: var(--brand-blue); }
  .card--back { left: 608px; }

  .front-header {
    position: absolute; left: 0; top: 0; width: 100%; height: 126px;
    background: var(--paper);
  }
  .brand {
    position: absolute;
    display: flex; align-items: center; gap: 20px;
    font-weight: 600;
    letter-spacing: 4px;
    white-space: nowrap;
  }
  .brand__dot { border-radius: 50%; flex: none; }
  .front-header .brand { left: 64px; top: 30px; font-size: 38px; color: var(--brand-blue); }
  .front-header .brand__dot { width: 54px; height: 54px; background: var(--brand-blue); }

  .roles {
    position: absolute; right: 233px; top: 145px;
    text-align: right; font-size: 12.5px; line-height: 16px;
  }
  .role + .role { margin-top: 20px; }
  .role__name { font-size: 15px; font-weight: 700; line-height: 17px; }

  .divider {
    position: absolute; left: 220px; top: 131px; width: 1px; height: 140px;
    background: var(--divider);
  }

  .contacts {
    position: absolute; left: 232px; top: 144px;
    list-style: none; font-size: 12.5px; line-height: 16px;
  }
  .contacts li { display: flex; align-items: center; gap: 8px; }
  .contacts li.gap-before { margin-top: 8px; }
  .icon { width: 9px; height: 9px; flex: none; }
  .icon-box { width: 9px; height: 9px; background: var(--text-light); border-radius: 2px; flex: none; }
  .flag { width: 16px; height: 10px; flex: none; margin-left: 2px; }
  .flag--us { background: linear-gradient(180deg, #b22234, #ffffff 50%, #b22234); }
  .flag--ru { background: linear-gradient(180deg, #ffffff 33%, #1c3f9a 33% 66%, #d52b1e 66%); }

  .back-pattern {
    position: absolute; inset: 0;
    background: linear-gradient(135deg, var(--brand-blue-light), var(--brand-blue));
  }
  .card--back .brand { left: 52px; top: 82px; font-size: 40px; color: var(--text-light); }
  .card--back .brand__dot { width: 58px; height: 58px; background: var(--text-light); }
  .tagline {
    position: absolute; left: 0; right: 0; top: 174px;
    text-align: center;
    font-family: Arial, "Helvetica Neue", sans-serif;
    font-size: 13px; letter-spacing: 0.3px;
  }
</style>
</head>
<body>

<section class="card card--front" aria-label="Card front">
  <header class="front-header">
    <div class="brand"><span class="brand__dot"></span><span>PEX LATTOR</span></div>
  </header>

  <div class="roles">
    <div class="role">
      <div class="role__name">Boris Melnovetz</div>
      <div>Founder/CEO/CTO</div>
    </div>
    <div class="role">
      <div class="role__name">Boris Melnovetz</div>
      <div>Real Estate Investor</div>
      <div>Cleveland, OH</div>
    </div>
  </div>

  <div class="divider"></div>

  <ul class="contacts">
    <li>
      <svg class="icon" viewBox="0 0 10 10"><rect x="0.5" y="2" width="9" height="6" fill="none" stroke="#fff" stroke-width="1.2"/><path d="M0.5 2 L5 5.5 L9.5 2" fill="none" stroke="#fff" stroke-width="1.2"/></svg>
      <span>melnovetz@quorbamail.com</span>
    </li>
    <li>
      <svg class="icon" viewBox="0 0 10 10"><path d="M2 0.8 L3.6 2.8 L2.7 4 C3.4 5.4 4.6 6.6 6 7.3 L7.2 6.4 L9.2 8 L8 9.5 C4.2 9 1 5.8 0.5 2 Z" fill="#fff"/></svg>
      <span>1(555)316-2947</span>
      <span class="flag flag--us" role="img" aria-label="United States flag"></span>
    </li>
    <li>
      <svg class="icon" viewBox="0 0 10 10"><path d="M2 0.8 L3.6 2.8 L2.7 4 C3.4 5.4 4.6 6.6 6 7.3 L7.2 6.4 L9.2 8 L8 9.5 C4.2 9 1 5.8 0.5 2 Z" fill="#fff"/></svg>
      <span>7(955)482-3170</span>
      <span class="flag flag--ru" role="img" aria-label="Russia flag"></span>
    </li>
    <li class="gap-before"><span class="icon-box"></span><span>plavbook.example/melnovetz</span></li>
    <li><span class="icon-box"></span><span>trelnet.example/in/melnovetz</span></li>
    <li><span class="icon-box"></span><span>boris_m</span></li>
  </ul>
</section>

<section class="card card--back" aria-label="Card back">
  <div class="back-pattern" role="img" aria-label="Faint repeating brand pattern on blue"></div>
  <div class="brand"><span class="brand__dot"></span><span>PEX LATTOR</span></div>
  <p class="tagline">E-COMMERCE AUTOMATION SOLUTIONS</p>
</section>

</body>
</html>
```